business card design for a small scale specialty cut flower farm

We need a business card design for Hollowmere Bloom Farm based in Langley, BC, Canada. We produce specialty, high-end cut flowers and sell locally to florists, local shops and markets and the end user through bouquet subscriptions. The final business card design should be memorable and have a timeless or vintage feel. We would prefer a square shape.
Updates

Target Market(s)

florists, shops and seasonal markets, local flower lovers

Industry/Entity Type

Floral

Contact Information for Business Card

Tamsin Ellery Voss, Grower
Langley, BC, Canada
website: hollowmerebloomfarm.example
instagram: @hollowmerebloomfarm
Tel: 555.317.4290
facebook: www.facebook.example/hollowmereblooms/

Font styles to use
Serif
Decorative
Script

Requirements
Must have
• soft black background colour on front side, the included logo and catch phrase: Fresh Local Seasonal
Nice to have
• phone number and website address on front of card, included photo 6539 incorporated onto the back, possibly photo 6609 as well.

```html
<!DOCTYPE html>
<html lang="en">
<head>
<meta charset="utf-8">
<title>Hollowmere Bloom Farm – Business Card</title>
<link rel="stylesheet" href="https://fonts.googleapis.com/css2?family=Lato:wght@400;700&family=Great+Vibes&display=swap">
<style>
  :root {
    --page-bg: #a3a3a3;
    --card-pink-light: #f3c9e0;
    --card-pink: #e9a9cb;
    --card-pink-deep: #d98cb6;
    --ink: #2b2427;
    --soft-black: #231f20;
    --white: #ffffff;
    --muted-white: #cfcfcf;
    --accent-pink: #f0a6cf;
    --bloom-pink: #e79ac3;
    --leaf-green: #3f6b3a;
  }
  * { margin: 0; padding: 0; box-sizing: border-box; }
  html, body { width: 1200px; height: 802px; overflow: hidden; }
  body {
    background: var(--page-bg);
    font-family: "Lato", Arial, sans-serif;
    position: relative;
  }
  .card {
    position: absolute;
    top: 274px;
    width: 442px;
    height: 264px;
    overflow: hidden;
    text-align: center;
  }
  .card--back { left: 136px; }
  .card--front { left: 624px; background: var(--soft-black); }

  .card__photo {
    position: absolute; inset: 0;
    background: radial-gradient(ellipse at 48% 55%, var(--card-pink-deep) 0%, var(--card-pink) 40%, var(--card-pink-light) 100%);
  }
  .card__content { position: absolute; inset: 0; }

  .brand-name {
    position: absolute; left: 0; right: 0;
    font-family: "Lato", Arial, sans-serif;
    font-weight: 400;
    letter-spacing: 3px;
    line-height: 1.2;
  }
  .card--back .brand-name { top: 74px; font-size: 18px; color: var(--ink); }
  .card--front .brand-name { top: 150px; font-size: 19px; color: var(--white); }

  .person-name {
    position: absolute; left: 0; right: 0; top: 136px;
    font-weight: 700; font-size: 13px; line-height: 16px; color: var(--ink); letter-spacing: .3px;
  }
  .person-role { position: absolute; left: 0; right: 0; top: 153px; font-size: 11.5px; line-height: 14px; color: var(--ink); }
  .rule { position: absolute; left: 192px; width: 58px; height: 1px; background: var(--ink); opacity: .7; }
  .rule--one { top: 171px; }
  .rule--two { top: 219px; }
  .phone { position: absolute; left: 0; right: 0; top: 177px; font-size: 12.5px; line-height: 15px; color: var(--ink); }
  .website { position: absolute; left: 0; right: 0; top: 198px; font-size: 12.5px; line-height: 15px; color: var(--ink); }
  .social {
    position: absolute; left: 0; right: 0; top: 226px;
    display: flex; justify-content: center; gap: 6px;
    font-size: 12.5px; line-height: 15px; color: var(--ink); white-space: nowrap;
  }
  .social__item { display: flex; align-items: center; gap: 3px; }
  .social__dot { width: 14px; height: 14px; border: 1.2px solid var(--ink); border-radius: 50%; flex: none; }

  .bloom {
    position: absolute; left: 168px; top: 38px; width: 110px; height: 66px;
    background: radial-gradient(circle at 45% 55%, #f8dce9 0%, var(--bloom-pink) 45%, rgba(63,107,58,.9) 75%, transparent 78%);
    border-radius: 50%;
  }
  .tagline {
    position: absolute; left: 0; right: 0; top: 182px;
    font-family: "Great Vibes", cursive; font-size: 15px; line-height: 18px; color: var(--muted-white);
  }
  .established {
    position: absolute; left: 0; right: 0; top: 205px;
    font-size: 8px; line-height: 10px; letter-spacing: 2.5px; color: var(--muted-white);
  }
  .catchphrase {
    position: absolute; left: 0; right: 0; top: 227px;
    font-size: 11.5px; line-height: 14px; color: var(--accent-pink); letter-spacing: .3px;
  }
</style>
</head>
<body>
  <section class="card card--back">
    <div class="card__photo" role="img" aria-label="Close-up photograph of a soft pink flower centre"></div>
    <div class="card__content">
      <div class="brand-name">HOLLOWMERE BLOOM FARM</div>
      <div class="person-name">TAMSIN ELLERY VOSS</div>
      <div class="person-role">Owner</div>
      <div class="rule rule--one"></div>
      <div class="phone">(555) 317-4290</div>
      <div class="website">www.hollowmerebloomfarm.example</div>
      <div class="rule rule--two"></div>
      <div class="social">
        <span class="social__item"><span class="social__dot"></span>@hollowmerebloomfarm</span>
        <span class="social__item"><span class="social__dot"></span>petalpage.example/hollowmereblooms</span>
      </div>
    </div>
  </section>

  <section class="card card--front">
    <div class="bloom" role="img" aria-label="Watercolour illustration of a pink wild rose with green leaves"></div>
    <div class="brand-name">HOLLOWMERE BLOOM FARM</div>
    <div class="tagline">Specialty Cut Flowers</div>
    <div class="established">EST.2019</div>
    <div class="catchphrase">FRESH LOCAL SEASONAL</div>
  </section>
</body>
</html>
```